Web Refresh

1 - Refresh my website
2 - Create a sell sheet
3- create a banner for trade show

Target Market(s)

Healthy Snack eating

Number of Pages Required

5+ page

Font styles to use
Serif
Sans Serif

Requirements
Must have
• Refer to document
Nice to have
• Refer to document
Should not have
• refer to document

```html
<!DOCTYPE html>
<html lang="en">
<head>
<meta charset="utf-8">
<title>Goobalo – Web Refresh</title>
<link href="https://fonts.googleapis.com/css2?family=Montserrat:wght@400;500;600;700;800&display=swap" rel="stylesheet">
<style>
:root{
  --green:#06a55b;
  --green-dark:#077a45;
  --red:#b3250f;
  --ink:#2b2b2b;
  --muted:#8d8d8d;
  --field:#edf1ef;
  --line:#e4e4e4;
  --white:#ffffff;
}
*{box-sizing:border-box;margin:0;padding:0}
html,body{width:851px;height:1200px;overflow:hidden;background:var(--white)}
body{position:relative;font-family:'Montserrat',sans-serif;color:var(--ink)}
.abs{position:absolute}
.page{position:absolute;background:var(--white);box-shadow:0 0 5px rgba(0,0,0,.13);overflow:hidden}

/* header */
.site-header{position:absolute;left:0;top:0;width:100%;height:26px;font-size:2.6px;font-weight:500}
.site-header .soc{position:absolute;top:11px;width:4px;height:4px;border:.6px solid var(--green);border-radius:50%}
.site-header .nav-link{position:absolute;top:12px;color:var(--ink);letter-spacing:.1px}
.site-header .nav-link.active{color:var(--green);border-bottom:.5px solid var(--green);padding-bottom:.8px}
.brand{position:absolute;top:7px;display:flex;align-items:center;gap:1.5px;font-size:5px;font-weight:800;color:var(--red);transform:translateX(-50%)}
.brand .mark{width:5px;height:5px;border-radius:50%;background:var(--red)}
.site-header .login{position:absolute;top:11.5px;color:var(--muted);display:flex;align-items:center;gap:1px}
.site-header .login i{width:3.4px;height:3.4px;border-radius:50%;background:var(--green)}
.site-header .cart{position:absolute;top:11px;width:5px;height:4px}

/* footer */
.site-footer{position:absolute;left:0;width:100%;background:var(--green);color:var(--white)}
.site-footer .f-brand{position:absolute;left:16px;top:12px;font-size:4px;font-weight:800;color:var(--white);display:flex;align-items:center;gap:1.2px}
.site-footer .f-brand i{width:4px;height:4px;border-radius:50%;background:var(--white)}
.site-footer .f-social{position:absolute;left:19px;top:25px;display:flex;gap:5px}
.site-footer .f-social i{width:3.6px;height:3.6px;border:.5px solid rgba(255,255,255,.8);border-radius:50%}
.f-col{position:absolute;top:13px;display:flex;flex-direction:column;gap:2.6px;font-size:2.1px;color:rgba(255,255,255,.75)}
.f-col h4{font-size:2.2px;font-weight:700;color:var(--white);margin-bottom:.6px}
.f-col .u{color:var(--white);text-decoration:underline}
.f-pay{position:absolute;top:16px;display:grid;grid-template-columns:repeat(3,auto);gap:3px 3px}
.f-pay i{display:block;height:5px;border-radius:1px;background:var(--white)}
.f-bottom{position:absolute;left:0;bottom:0;width:100%;height:9px;background:var(--green-dark);font-size:2px;color:rgba(255,255,255,.45);text-align:center;line-height:9px}

/* type */
.h-red{position:absolute;font-size:4px;font-weight:700;color:var(--red);letter-spacing:.1px}
.h-red.rule{border-bottom:.6px solid var(--red);padding-bottom:1.2px}
.copy{position:absolute;font-size:2.3px;line-height:1.45;color:var(--muted);text-align:justify}
.copy p+p{margin-top:2.5px}
.copy b{color:var(--ink)}

/* tabs */
.tab{position:absolute;font-size:3.2px;font-weight:600;color:var(--muted)}
.tab.on{color:var(--red);border-bottom:.6px solid var(--red);padding-bottom:1px}

/* product card */
.card{position:absolute;width:56px;text-align:center}
.pack{margin:0 auto;width:13px;height:29px;border-radius:1.5px;background:linear-gradient(180deg,#2f9f7b 0 22%,#b07a4b 22% 82%,#2f9f7b 82%)}
.pack.red{background:linear-gradient(180deg,#d86a6a 0 22%,#b07a4b 22% 82%,#d86a6a 82%)}
.pack.blue{background:linear-gradient(180deg,#4e9ed0 0 22%,#b07a4b 22% 82%,#4e9ed0 82%)}
.pack.multi{width:35px;height:23px;margin-top:3px;margin-bottom:3px;background:linear-gradient(90deg,#4e9ed0 0 30%,transparent 30% 35%,#2f9f7b 35% 65%,transparent 65% 70%,#d86a6a 70%)}
.card-name{margin-top:5px;font-size:2.4px;line-height:1.3;color:var(--ink)}
.card-price{margin-top:2px;font-size:2.4px;font-weight:600;color:var(--green)}
.stars{margin-top:1.5px;font-size:3px;letter-spacing:.4px;color:var(--green)}
.stars span{color:#cfcfcf}

/* bands */
.red-band{position:absolute;left:0;width:100%;background:var(--red);color:var(--white);font-size:2.4px}
.red-band .perk{position:absolute;top:5px;display:flex;align-items:center;gap:5px;line-height:1.3}
.red-band .perk i{width:13px;height:13px;border-radius:50%;background:#8f1c0a;flex:none}
.red-band .split{position:absolute;left:50%;top:3px;bottom:3px;width:.5px;background:rgba(255,255,255,.7)}

/* forms */
.label{position:absolute;font-size:2.3px;color:var(--ink)}
.field{position:absolute;height:7.5px;background:var(--field);border-radius:.6px}
.btn{position:absolute;height:7.5px;background:var(--red);color:var(--white);font-size:2.4px;font-weight:600;text-align:center;line-height:7.5px;border-radius:.8px}
.check{position:absolute;width:3.5px;height:3.5px;border:.5px solid var(--green);border-radius:.6px}

/* faq */
.faq-q{position:absolute;left:12px;width:197px;font-size:2.3px;font-weight:700;color:var(--ink);padding-bottom:2.5px;border-bottom:.4px solid var(--line);display:flex;justify-content:space-between}
.faq-a{position:absolute;left:12px;font-size:2.3px;color:var(--muted)}

/* nutrition */
.acc{position:absolute;left:30px;width:34px;font-size:3px;font-weight:600;display:flex;justify-content:space-between}
.acc::after{content:"";border:1.2px solid transparent;border-top:1.5px solid var(--ink);margin-top:1px}
.nut{position:absolute;left:81px;top:185px;width:126px;font-size:2.2px;color:var(--ink);border-collapse:collapse}
.nut th{text-align:left;font-weight:700;height:9px;vertical-align:top}
.nut td{height:8.45px}

/* icons band */
.benefits{position:absolute;left:0;width:100%;background:var(--green)}
.benefit{position:absolute;width:40px;text-align:center;font-size:2.4px;color:var(--white)}
.benefit .ic{display:block;margin:0 auto 4px;width:14px;height:14px}
</style>
</head>
<body>

<!-- ===== HOME ===== -->
<section class="page" style="left:35px;top:47px;width:215px;height:663px">
  <header class="site-header">
    <span class="soc" style="left:12px"></span><span class="soc" style="left:22px"></span>
    <a class="nav-link active" style="left:63px">HOME</a><a class="nav-link" style="left:81px">SHOP</a>
    <div class="brand" style="left:107px"><span class="mark"></span>Goobalo</div>
    <a class="nav-link" style="left:128px">ABOUT</a><a class="nav-link" style="left:147px">FAQ</a>
    <span class="login" style="left:175px"><i></i>Login</span>
    <svg class="cart" style="left:197px" viewBox="0 0 10 8"><path d="M0 2h10L8.5 8h-7z" fill="#06a55b"/></svg>
  </header>
  <div class="abs" role="img" aria-label="Peanuts in shells spilling across a wooden table with a green painted edge" style="left:0;top:26px;width:215px;height:86px;background:linear-gradient(110deg,#2f7d5f 0%,#3e8063 40%,#8d7450 62%,#c49e68 80%,#a88658 100%)"></div>
  <div class="abs" style="left:12px;top:41px;color:#fff;font-size:7px;font-weight:800;line-height:1.2">WE’RE<br>ALL ABOUT<br>PEANUT</div>
  <div class="abs" style="left:12px;top:70px;color:#fff;font-size:2.3px;line-height:1.4">Give Goobalo “Peanut Crackers” a<br>Go and you will come back for more!</div>
  <div class="btn" style="left:12px;top:83px;width:24px;height:6px;line-height:6px;font-size:2.2px">SHOP NOW</div>
  <div class="abs" style="left:99px;top:106px;display:flex;gap:2px"><i style="width:1.4px;height:1.4px;border-radius:50%;background:#ddd"></i><i style="width:1.4px;height:1.4px;border-radius:50%;background:#ddd"></i><i style="width:1.4px;height:1.4px;border-radius:50%;background:#fff"></i><i style="width:1.4px;height:1.4px;border-radius:50%;background:#ddd"></i><i style="width:1.4px;height:1.4px;border-radius:50%;background:#ddd"></i></div>
  <div class="red-band" style="top:112px;height:23px">
    <div class="perk" style="left:12px"><i></i>Free Shipping Throughout the UK on All<br>Orders Over £20!</div>
    <span class="split"></span>
    <div class="perk" style="left:116px"><i></i>Our peanut snacks and cold pressed oil<br>are all hand made from organic peanuts!</div>
  </div>

  <span class="tab on" style="left:70px;top:157px">PEANUT CRACKERS</span>
  <span class="tab" style="left:122px;top:157px">PEANUT OIL</span>

  <div class="card" style="left:20px;top:178px"><div class="pack"></div><p class="card-name">Organic Peanut Crackers<br>Peppercorn (15 x 25g)</p><p class="card-price">£23.25</p><p class="stars">★★★★<span>★</span></p></div>
  <div class="card" style="left:79px;top:178px"><div class="pack multi"></div><p class="card-name">Organic Peanut Crackers<br>(Mix taster pack 3 x 25g)</p><p class="card-price">£5.99</p><p class="stars">★★★★★</p></div>
  <div class="card" style="left:139px;top:178px"><div class="pack red"></div><p class="card-name">Organic Peanut Crackers<br>Chili Flakes (15 x 25g)</p><p class="card-price">£23.25</p><p class="stars">★★★★★</p></div>
  <div class="card" style="left:20px;top:245px"><div class="pack blue"></div><p class="card-name">Organic Peanut Crackers<br>(Original taster pack 3 x 25g)</p><p class="card-price">£5.99</p><p class="stars">★★★★<span>★</span></p></div>
  <div class="card" style="left:79px;top:245px"><div class="pack multi"></div><p class="card-name">Organic Peanut Crackers<br>(Mix pack 15 x 25g)</p><p class="card-price">£23.25</p><p class="stars">★★★★★</p></div>
  <div class="card" style="left:139px;top:245px"><div class="pack blue"></div><p class="card-name">Organic Peanut Crackers<br>Original (15 x 25g)</p><p class="card-price">£23.25</p><p class="stars">★★★★★</p></div>

  <div class="benefits" style="top:323px;height:77px">
    <div class="benefit" style="left:15px;top:9px"><svg class="ic" viewBox="0 0 14 14"><circle cx="7" cy="7" r="7" fill="#fff"/><path d="M3 9l3-4 2 2 3-4" stroke="#06a55b" stroke-width="1.6" fill="none"/></svg>high protein</div>
    <div class="benefit" style="left:64px;top:9px"><svg class="ic" viewBox="0 0 14 14"><circle cx="7" cy="7" r="7" fill="#fff"/><path d="M4 10C4 5 7 3.5 10.5 3.5 10.5 7 9 10 4 10z" fill="#06a55b"/></svg>High fibre</div>
    <div class="benefit" style="left:113px;top:9px"><svg class="ic" viewBox="0 0 14 14"><circle cx="7" cy="7" r="7" fill="#fff"/><rect x="4" y="4" width="6" height="6" fill="#b3250f"/><path d="M3 11L11 3" stroke="#06a55b" stroke-width="1.2"/></svg>low carb</div>
    <div class="benefit" style="left:162px;top:9px"><svg class="ic" viewBox="0 0 14 14"><circle cx="7" cy="7" r="7" fill="#fff"/><path d="M5 5l2 2 3-3" stroke="#06a55b" stroke-width="1.1" fill="none"/><text x="7" y="10.5" font-size="3" font-family="Montserrat,sans-serif" font-weight="700" text-anchor="middle" fill="#06a55b">KETO</text></svg>Keto</div>
    <div class="benefit" style="left:15px;top:45px"><svg class="ic" viewBox="0 0 14 14"><circle cx="7" cy="7" r="7" fill="#fff"/><path d="M3 7h8a4 4 0 0 1-8 0z" fill="#b3250f"/><path d="M4 6.5C4 4 7 3 8 3.5 8 5 6 6.5 4 6.5z" fill="#06a55b"/></svg>vegan</div>
    <div class="benefit" style="left:64px;top:45px"><svg class="ic" viewBox="0 0 14 14"><circle cx="7" cy="7" r="7" fill="#fff"/><path d="M7 3c2 3 3 4.5 3 6a3 3 0 0 1-6 0c0-1.5 1-3 3-6z" fill="#06a55b"/></svg>low fat</div>
    <div class="benefit" style="left:113px;top:45px"><svg class="ic" viewBox="0 0 14 14"><circle cx="7" cy="7" r="7" fill="#fff"/><path d="M7 11V4M5 6l2 1.5L9 6M5 8.5l2 1.5 2-1.5" stroke="#06a55b" stroke-width="1" fill="none"/><path d="M3.5 10.5L10.5 3.5" stroke="#06a55b" stroke-width="1"/></svg>gluten free</div>
    <div class="benefit" style="left:162px;top:45px"><svg class="ic" viewBox="0 0 14 14"><circle cx="7" cy="7" r="7" fill="#fff"/><path d="M4 10C4 5.5 7 4 10.5 3.5 10.5 7.5 8.5 10 4 10z" fill="#06a55b"/></svg>Organic</div>
  </div>

  <div class="abs" role="img" aria-label="Pile of square peanut crackers" style="left:12px;top:431px;width:66px;height:57px;background:radial-gradient(ellipse at 50% 50%,#e7be82 0%,#dcae6c 55%,#fff 72%)"></div>
  <p class="h-red" style="left:102px;top:431px;font-size:3px">PEANUTS | CRACKERS | SNACKS</p>
  <div class="copy" style="left:102px;top:439px;width:100px">
    <p><b>At Goobalo, we enjoy making very tasty, healthy products.</b></p>
    <p>Our extra crunchy organic peanut crackers are hand made from high quality peanuts and spices with no artificial additives. Crackers are made from 97 % organic peanuts and packed with protein (47g of protein per 100g) and fiber (10.6g per 100g) making it a perfect satisfying snack.</p>
    <p>Our Crackers are currently available in 3 savoury flavours: Original, Peppercorn and Chili flakes.</p>
    <p><b>Give Goobalo “Peanut Crackers” a Go and you will come back for more!</b></p>
  </div>

  <p class="h-red" style="left:12px;top:517px;font-size:3px">ORGANIC COLD PRESSED PEANUT OIL</p>
  <div class="copy" style="left:12px;top:525px;width:102px">
    <p><b>A light golden oil with peanut flavour and smell, our peanut oil is carefully extracted using very natural and traditional method. This allows the oil to keep all the goodness and nutritional values.</b></p>
    <p>Cold pressed peanut oil is a good source of Vitamin E and phytosterols, beta sitosterol and polyphenols. The high oleic acid content helps to reduce cholesterol.</p>
    <p>Excellent as a neutral cooking oil that can be used in various cuisine such as Asian, Middle Eastern, African, salad dressing and sautéing.</p>
  </div>
  <div class="abs" role="img" aria-label="Bottles of peanut oil on a wooden surface" style="left:138px;top:519px;width:65px;height:54px;background:linear-gradient(180deg,#3d2a1c,#7a4f2c 60%,#a8743f)"></div>

  <footer class="site-footer" style="top:594px;height:69px">
    <div class="f-brand"><i></i>Goobalo</div><div class="f-social"><i></i><i></i></div>
    <div class="f-col" style="left:49px"><h4>CUSTOMER CARE</h4><a class="u">Contact Us</a><a>How to Order</a><a>FAQ</a><a>Shipping</a><a>Terms &amp; Conditions</a><a>Wholesale</a></div>
    <div class="f-col" style="left:83px"><h4>ABOUT US</h4><a>Hello!</a><a>Store Locator</a></div>
    <div class="f-col" style="left:110px"><h4>MY ACCOUNT</h4><a>Sign In</a><a>Register</a><a>Payment Confirmation</a><a>Reviews</a></div>
    <div class="f-pay" style="left:152px"><i style="width:7px"></i><i style="width:18px"></i><i style="width:15px"></i><i style="width:14px"></i><i style="width:10px"></i><i style="width:15px"></i></div>
    <div class="f-bottom">Copyright ©2021 Goobalo</div>
  </footer>
</section>

<!-- ===== PRODUCT ===== -->
<section class="page" style="left:313px;top:47px;width:221px;height:455px">
  <header class="site-header">
    <span class="soc" style="left:12px"></span><span class="soc" style="left:22px"></span>
    <a class="nav-link" style="left:64px">HOME</a><a class="nav-link active" style="left:83px">SHOP</a>
    <div class="brand" style="left:110px"><span class="mark"></span>Goobalo</div>
    <a class="nav-link" style="left:131px">ABOUT</a><a class="nav-link" style="left:151px">FAQ</a>
    <span class="login" style="left:180px"><i></i>Login</span>
    <svg class="cart" style="left:203px" viewBox="0 0 10 8"><path d="M0 2h10L8.5 8h-7z" fill="#06a55b"/></svg>
  </header>
  <p class="abs" style="left:12px;top:30px;font-size:2.3px;color:var(--ink)"><span style="color:var(--red);font-weight:700;border-bottom:.4px solid var(--red)">PEANUT CRACKERS</span>/Organic Peanut Crackers Peppercorn (15 x 25g)</p>
  <div class="abs" style="left:29px;top:41px;width:78px;height:65px;border:.4px solid var(--line);box-shadow:0 .5px 1.5px rgba(0,0,0,.12)"></div>
  <div class="abs" role="img" aria-label="Peppercorn cracker pack" style="left:57px;top:46px;width:22px;height:55px;border-radius:2px;background:linear-gradient(180deg,#2f9f7b 0 22%,#b07a4b 22% 84%,#2f9f7b 84%)"></div>
  <p class="abs" style="left:121px;top:45px;font-size:3.5px;font-weight:700;line-height:1.25">Organic Peanut Crackers Peppercorn<br>(15 x 25g)</p>
  <p class="abs" style="left:121px;top:56px;font-size:3px;color:var(--green)">★★★★<span style="color:#cfcfcf">★</span> <span style="font-size:2px;color:var(--muted)">(8)</span></p>
  <p class="abs" style="left:121px;top:63px;font-size:4px;color:var(--green);font-weight:500">£23.25</p>
  <p class="abs" style="left:121px;top:73px;font-size:2px;color:var(--muted)">Quantity</p>
  <div class="abs" style="left:135px;top:71.5px;width:18px;height:5px;border:.4px solid #ccc;font-size:2px;color:var(--muted);padding-left:2px;line-height:4.3px">1</div>
  <div class="btn" style="left:121px;top:87px;width:70px">ADD TO CART</div>
  <div class="abs" style="left:121px;top:98px;width:70px;height:7.5px;font-size:2.4px;font-weight:600;color:var(--red);text-align:center;line-height:7.5px;box-shadow:0 .6px 1.5px rgba(0,0,0,.18)">ADD TO WISHLIST</div>
  <div class="abs" style="left:29px;top:114px;width:11px;height:11px;border:.4px solid var(--line);background:linear-gradient(90deg,#fff 40%,#6fa882 40% 60%,#fff 60%)" role="img" aria-label="Pack thumbnail"></div>
  <div class="abs" style="left:43px;top:114px;width:11px;height:11px;background:#2e7f66" role="img" aria-label="Pack thumbnail"></div>
  <div class="abs" style="left:58px;top:114px;width:11px;height:11px;background:#b9dccd" role="img" aria-label="Pack thumbnail"></div>

  <p class="acc" style="top:131px">Details</p>
  <div class="copy" style="left:82px;top:138px;width:126px;text-align:left"><p>A crunchy, healthy and tasty crackers with a touch of peppercorn. Our organic peanuts crackers are high in protein and packed with fibre. Hand made with care you can now enjoy a nutty savoury snacks without having to think twice.</p></div>
  <p class="acc" style="top:159px">Ingredients</p>
  <div class="copy" style="left:82px;top:166px;width:126px;text-align:left"><p>Organic peanuts 97%, sea salt, peppercorn, xanthan gum, bicarbonate of soda.</p></div>
  <p class="acc" style="top:179px">Nutrition</p>
  <table class="nut">
    <tr><th>Typical values</th><th>Per 100g</th><th>Per 25g</th></tr>
    <tr><td>Energy</td><td>435kcal/1823kj</td><td>109kcal/456kj</td></tr>
    <tr><td>Protein</td><td>46.7</td><td>11.7</td></tr>
    <tr><td>Fat of which</td><td>17.3</td><td>4.3</td></tr>
    <tr><td>Mono-unsaturated</td><td>6.4</td><td>1.6</td></tr>
    <tr><td>Poly-unsaturated</td><td>7.2</td><td>1.8</td></tr>
    <tr><td>Saturated</td><td>3.8</td><td>0.9</td></tr>
    <tr><td>Carbohydrate of which</td><td>17.9</td><td>4.5</td></tr>
    <tr><td>Sugar</td><td>8.5</td><td>2.1</td></tr>
    <tr><td>Fibre</td><td>10.6</td><td>2.6</td></tr>
    <tr><td>Salt</td><td>2.6</td><td>0.6</td></tr>
  </table>

  <div class="card" style="left:22px;top:306px"><div class="pack blue"></div><p class="card-name">Organic Peanut Crackers<br>(Original taster pack 3 x 25g)</p><p class="card-price">£5.99</p><p class="stars">★★★★<span>★</span></p></div>
  <div class="card" style="left:82px;top:306px"><div class="pack multi"></div><p class="card-name">Organic Peanut Crackers<br>(Mix pack 15 x 25g)</p><p class="card-price">£23.25</p><p class="stars">★★★★★</p></div>
  <div class="card" style="left:143px;top:306px"><div class="pack blue"></div><p class="card-name">Organic Peanut Crackers<br>Original (15 x 25g)</p><p class="card-price">£23.25</p><p class="stars">★★★★★</p></div>

  <footer class="site-footer" style="top:386px;height:69px">
    <div class="f-brand"><i></i>Goobalo</div><div class="f-social"><i></i><i></i></div>
    <div class="f-col" style="left:50px"><h4>CUSTOMER CARE</h4><a class="u">Contact Us</a><a>How to Order</a><a>FAQ</a><a>Shipping</a><a>Terms &amp; Conditions</a><a>Wholesale</a></div>
    <div class="f-col" style="left:85px"><h4>ABOUT US</h4><a>Hello!</a><a>Store Locator</a></div>
    <div class="f-col" style="left:113px"><h4>MY ACCOUNT</h4><a>Sign In</a><a>Register</a><a>Payment Confirmation</a><a>Reviews</a></div>
    <div class="f-pay" style="left:156px"><i style="width:7px"></i><i style="width:18px"></i><i style="width:15px"></i><i style="width:14px"></i><i style="width:10px"></i><i style="width:15px"></i></div>
    <div class="f-bottom">Copyright ©2021 Goobalo</div>
  </footer>
</section>

<!-- ===== FAQ ===== -->
<section class="page" style="left:597px;top:47px;width:221px;height:238px">
  <header class="site-header">
    <span class="soc" style="left:12px"></span><span class="soc" style="left:22px"></span>
    <a class="nav-link" style="left:64px">HOME</a><a class="nav-link" style="left:83px">SHOP</a>
    <div class="brand" style="left:110px"><span class="mark"></span>Goobalo</div>
    <a class="nav-link" style="left:131px">ABOUT</a><a class="nav-link active" style="left:151px">FAQ</a>
    <span class="login" style="left:180px"><i></i>Login</span>
    <svg class="cart" style="left:203px" viewBox="0 0 10 8"><path d="M0 2h10L8.5 8h-7z" fill="#06a55b"/></svg>
  </header>
  <p class="h-red rule" style="left:12px;top:33px">FAQ</p>
  <p class="faq-q" style="top:48px;border:0">WHERE DO YOU SHIP TO?<span>–</span></p>
  <p class="faq-a" style="top:57px">We offer shipping throughout the UK.</p>
  <p class="faq-q" style="top:68px;border:0">WHEN WILL MY ORDER BE SHIPPED?<span>–</span></p>
  <p class="faq-a" style="top:77px">For orders placed by 4pm on a business day we aim to process, pack and ship your order the following day.</p>
  <p class="faq-a" style="top:85px">Orders placed after 5pm or on weekends and holidays will be processed the following business day.</p>
  <p class="faq-a" style="top:93px">Please note at exceptionally busy times these timings might vary.</p>
  <p class="faq-q" style="top:105px">WHICH SHIPPING METHODS DO YOU USE?<span>+</span></p>
  <p class="faq-q" style="top:116px">I RECEIVED MY ORDER BUT IT’S INCORRECT OR DAMAGED<span>+</span></p>
  <p class="faq-q" style="top:127px">CAN I CHANGE MY ORDER AFTER I HAVE PLACED IT?<span>+</span></p>
  <p class="faq-q" style="top:139px">CAN I RETURN MY ORDER?<span>+</span></p>
  <p class="faq-q" style="top:150px;border:0">I HAVE A QUESTION ABOUT A PRODUCT OR SHIPPING<span>+</span></p>
  <footer class="site-footer" style="top:169px;height:69px">
    <div class="f-brand"><i></i>Goobalo</div><div class="f-social"><i></i><i></i></div>
    <div class="f-col" style="left:50px"><h4>CUSTOMER CARE</h4><a class="u">Contact Us</a><a>How to Order</a><a>FAQ</a><a>Shipping</a><a>Terms &amp; Conditions</a><a>Wholesale</a></div>
    <div class="f-col" style="left:85px"><h4>ABOUT US</h4><a>Hello!</a><a>Store Locator</a></div>
    <div class="f-col" style="left:113px"><h4>MY ACCOUNT</h4><a>Sign In</a><a>Register</a><a>Payment Confirmation</a><a>Reviews</a></div>
    <div class="f-pay" style="left:156px"><i style="width:7px"></i><i style="width:18px"></i><i style="width:15px"></i><i style="width:14px"></i><i style="width:10px"></i><i style="width:15px"></i></div>
    <div class="f-bottom">Copyright ©2021 Goobalo</div>
  </footer>
</section>

<!-- ===== ABOUT ===== -->
<section class="page" style="left:597px;top:334px;width:221px;height:300px">
  <header class="site-header">
    <span class="soc" style="left:12px"></span><span class="soc" style="left:22px"></span>
    <a class="nav-link" style="left:64px">HOME</a><a class="nav-link" style="left:83px">SHOP</a>
    <div class="brand" style="left:110px"><span class="mark"></span>Goobalo</div>
    <a class="nav-link active" style="left:131px">ABOUT</a><a class="nav-link" style="left:151px">FAQ</a>
    <span class="login" style="left:180px"><i></i>Login</span>
    <svg class="cart" style="left:203px" viewBox="0 0 10 8"><path d="M0 2h10L8.5 8h-7z" fill="#06a55b"/></svg>
  </header>
  <div class="abs" role="img" aria-label="Chili flakes cracker pack on pink" style="left:12px;top:39px;width:66px;height:63px;background:linear-gradient(135deg,#cc7a7e,#c46c70)"></div>
  <div class="abs" role="img" aria-label="Original cracker pack with sea salt on blue" style="left:78px;top:39px;width:65px;height:63px;background:linear-gradient(135deg,#6fb4d6,#5aa6cc)"></div>
  <div class="abs" role="img" aria-label="Peppercorn cracker pack with peppercorns on teal" style="left:143px;top:39px;width:65px;height:63px;background:linear-gradient(135deg,#4aa68e,#3d9a82)"></div>
  <div class="copy" style="left:50px;top:113px;width:121px">
    <p>We are a small family run business that produces hand made Crackers and Cold pressed peanut oil.</p>
    <p>Our Peanut Crackers are made from 97% organic peanuts with only 4 ingredients and are a great healthier alternative to most savoury snacks that are available on the market without compromising the taste. Our snacks are packed with the “good stuff” as due to the innovative manufacturing process we are able to reduce the fat content of peanuts substantially therefore the snacks are very high in protein (12g per 25g pack), high in fibre (3g per 25g pack), low in carbs (5g per 25g pack) and suitable for gluten free, vegan, and low carbs diets.</p>
    <p>You can enjoy our crackers with a glass of beer/wine but also due to the high content of protein and low carbs, the crackers can be a perfect post workout snack for any gym goers or anyone else who simply enjoys low carbs tasty snack.</p>
    <p>Our Peanut Oil is a perfect healthy alternative to a regular frying and cooking oils as it has a high smoking point and goes really well with salads too. There are many health benefits of Peanut Oil and the main is that is high in monounsaturated and polyunsaturated “good” fat and low in saturated “bad” fat, which is believed to help prevent heart disease and lower cholesterol.</p>
  </div>
  <p class="h-red" style="left:0;width:221px;text-align:center;top:218px;font-size:3.2px">GIVE GOOBALO A GO AND YOU WILL COME BACK!</p>
  <footer class="site-footer" style="top:231px;height:69px">
    <div class="f-brand"><i></i>Goobalo</div><div class="f-social"><i></i><i></i></div>
    <div class="f-col" style="left:50px"><h4>CUSTOMER CARE</h4><a class="u">Contact Us</a><a>How to Order</a><a>FAQ</a><a>Shipping</a><a>Terms &amp; Conditions</a><a>Wholesale</a></div>
    <div class="f-col" style="left:85px"><h4>ABOUT US</h4><a>Hello!</a><a>Store Locator</a></div>
    <div class="f-col" style="left:113px"><h4>MY ACCOUNT</h4><a>Sign In</a><a>Register</a><a>Payment Confirmation</a><a>Reviews</a></div>
    <div class="f-pay" style="left:156px"><i style="width:7px"></i><i style="width:18px"></i><i style="width:15px"></i><i style="width:14px"></i><i style="width:10px"></i><i style="width:15px"></i></div>
    <div class="f-bottom">Copyright ©2021 Goobalo</div>
  </footer>
</section>

<!-- ===== CONTACT ===== -->
<section class="page" style="left:313px;top:553px;width:221px;height:233px">
  <header class="site-header">
    <span class="soc" style="left:12px"></span><span class="soc" style="left:22px"></span>
    <a class="nav-link" style="left:64px">HOME</a><a class="nav-link" style="left:83px">SHOP</a>
    <div class="brand" style="left:110px"><span class="mark"></span>Goobalo</div>
    <a class="nav-link" style="left:131px">ABOUT</a><a class="nav-link" style="left:151px">FAQ</a>
    <span class="login" style="left:180px"><i></i>Login</span>
    <svg class="cart" style="left:203px" viewBox="0 0 10 8"><path d="M0 2h10L8.5 8h-7z" fill="#06a55b"/></svg>
  </header>
  <p class="h-red rule" style="left:12px;top:33px">CONTACT US</p>
  <span class="label" style="left:42px;top:45px">Name</span><span class="label" style="left:115px;top:45px">Phone</span>
  <div class="field" style="left:42px;top:50px;width:65px"></div><div class="field" style="left:115px;top:50px;width:65px"></div>
  <span class="label" style="left:42px;top:62px">Email Address</span><div class="field" style="left:42px;top:67px;width:138px"></div>
  <span class="label" style="left:42px;top:79px">Subject</span><div class="field" style="left:42px;top:84px;width:138px"></div>
  <span class="label" style="left:42px;top:96px">Message</span><div class="field" style="left:42px;top:101px;width:138px;height:38px"></div>
  <div class="btn" style="left:42px;top:143px;width:65px">SUBMIT</div>
  <footer class="site-footer" style="top:164px;height:69px">
    <div class="f-brand"><i></i>Goobalo</div><div class="f-social"><i></i><i></i></div>
    <div class="f-col" style="left:50px"><h4>CUSTOMER CARE</h4><a class="u">Contact Us</a><a>How to Order</a><a>FAQ</a><a>Shipping</a><a>Terms &amp; Conditions</a><a>Wholesale</a></div>
    <div class="f-col" style="left:85px"><h4>ABOUT US</h4><a>Hello!</a><a>Store Locator</a></div>
    <div class="f-col" style="left:113px"><h4>MY ACCOUNT</h4><a>Sign In</a><a>Register</a><a>Payment Confirmation</a><a>Reviews</a></div>
    <div class="f-pay" style="left:156px"><i style="width:7px"></i><i style="width:18px"></i><i style="width:15px"></i><i style="width:14px"></i><i style="width:10px"></i><i style="width:15px"></i></div>
    <div class="f-bottom">Copyright ©2021 Goobalo</div>
  </footer>
</section>

<!-- ===== SHOP ===== -->
<section class="page" style="left:597px;top:683px;width:221px;height:281px">
  <header class="site-header">
    <span class="soc" style="left:12px"></span><span class="soc" style="left:22px"></span>
    <a class="nav-link" style="left:64px">HOME</a><a class="nav-link active" style="left:83px">SHOP</a>
    <div class="brand" style="left:110px"><span class="mark"></span>Goobalo</div>
    <a class="nav-link" style="left:131px">ABOUT</a><a class="nav-link" style="left:151px">FAQ</a>
    <span class="login" style="left:180px"><i></i>Login</span>
    <svg class="cart" style="left:203px" viewBox="0 0 10 8"><path d="M0 2h10L8.5 8h-7z" fill="#06a55b"/></svg>
  </header>
  <span class="tab on" style="left:72px;top:34px">PEANUT CRACKERS</span>
  <span class="tab" style="left:126px;top:34px">PEANUT OIL</span>
  <div class="card" style="left:22px;top:55px"><div class="pack"></div><p class="card-name">Organic Peanut Crackers<br>Peppercorn (15 x 25g)</p><p class="card-price">£23.25</p><p class="stars">★★★★<span>★</span></p></div>
  <div class="card" style="left:82px;top:55px"><div class="pack multi"></div><p class="card-name">Organic Peanut Crackers<br>(Mix taster pack 3 x 25g)</p><p class="card-price">£5.99</p><p class="stars">★★★★★</p></div>
  <div class="card" style="left:144px;top:55px"><div class="pack red"></div><p class="card-name">Organic Peanut Crackers<br>Chili Flakes (15 x 25g)</p><p class="card-price">£23.25</p><p class="stars">★★★★★</p></div>
  <div class="card" style="left:22px;top:124px"><div class="pack blue"></div><p class="card-name">Organic Peanut Crackers<br>(Original taster pack 3 x 25g)</p><p class="card-price">£5.99</p><p class="stars">★★★★<span>★</span></p></div>
  <div class="card" style="left:82px;top:124px"><div class="pack multi"></div><p class="card-name">Organic Peanut Crackers<br>(Mix pack 15 x 25g)</p><p class="card-price">£23.25</p><p class="stars">★★★★★</p></div>
  <div class="card" style="left:144px;top:124px"><div class="pack blue"></div><p class="card-name">Organic Peanut Crackers<br>Original (15 x 25g)</p><p class="card-price">£23.25</p><p class="stars">★★★★★</p></div>
  <footer class="site-footer" style="top:212px;height:69px">
    <div class="f-brand"><i></i>Goobalo</div><div class="f-social"><i></i><i></i></div>
    <div class="f-col" style="left:50px"><h4>CUSTOMER CARE</h4><a class="u">Contact Us</a><a>How to Order</a><a>FAQ</a><a>Shipping</a><a>Terms &amp; Conditions</a><a>Wholesale</a></div>
    <div class="f-col" style="left:85px"><h4>ABOUT US</h4><a>Hello!</a><a>Store Locator</a></div>
    <div class="f-col" style="left:113px"><h4>MY ACCOUNT</h4><a>Sign In</a><a>Register</a><a>Payment Confirmation</a><a>Reviews</a></div>
    <div class="f-pay" style="left:156px"><i style="width:7px"></i><i style="width:18px"></i><i style="width:15px"></i><i style="width:14px"></i><i style="width:10px"></i><i style="width:15px"></i></div>
    <div class="f-bottom">Copyright ©2021 Goobalo</div>
  </footer>
</section>

<!-- ===== LOGIN ===== -->
<section class="page" style="left:35px;top:786px;width:221px;height:208px">
  <header class="site-header">
    <span class="soc" style="left:12px"></span><span class="soc" style="left:22px"></span>
    <a class="nav-link" style="left:64px">HOME</a><a class="nav-link" style="left:83px">SHOP</a>
    <div class="brand" style="left:110px"><span class="mark"></span>Goobalo</div>
    <a class="nav-link" style="left:131px">ABOUT</a><a class="nav-link" style="left:151px">FAQ</a>
    <span class="login" style="left:180px"><i></i>Login</span>
    <svg class="cart" style="left:203px" viewBox="0 0 10 8"><path d="M0 2h10L8.5 8h-7z" fill="#06a55b"/></svg>
  </header>
  <p class="h-red" style="left:12px;top:36px;font-size:4.8px">WELCOME BACK</p>
  <p class="h-red" style="left:123px;top:36px;font-size:4.8px">NEW CUSTOMER</p>
  <span class="abs" style="left:111px;top:36px;width:.4px;height:74px;background:var(--line)"></span>
  <span class="label" style="left:12px;top:49px">Email Address</span><div class="field" style="left:12px;top:54px;width:69px"></div>
  <span class="label" style="left:12px;top:65px">Password</span><div class="field" style="left:12px;top:70px;width:69px"></div>
  <span class="label" style="left:66px;top:80px;font-size:1.8px;color:var(--green)">Forgot Password?</span>
  <div class="btn" style="left:12px;top:86px;width:69px">SIGN IN</div>
  <p class="copy" style="left:123px;top:49px;width:86px;text-align:left">By creating an account with us, you will be able to move through the checkout process faster</p>
  <div class="btn" style="left:123px;top:60px;width:69px">SIGN IN</div>
  <div class="red-band" style="top:115px;height:24px">
    <div class="perk" style="left:12px"><i></i>Free Shipping Throughout the UK on All<br>Orders Over £20!</div>
    <span class="split"></span>
    <div class="perk" style="left:119px"><i></i>Our peanut snacks and cold pressed oil<br>are all hand made from organic peanuts!</div>
  </div>
  <footer class="site-footer" style="top:139px;height:69px">
    <div class="f-brand"><i></i>Goobalo</div><div class="f-social"><i></i><i></i></div>
    <div class="f-col" style="left:50px"><h4>CUSTOMER CARE</h4><a class="u">Contact Us</a><a>How to Order</a><a>FAQ</a><a>Shipping</a><a>Terms &amp; Conditions</a><a>Wholesale</a></div>
    <div class="f-col" style="left:85px"><h4>ABOUT US</h4><a>Hello!</a><a>Store Locator</a></div>
    <div class="f-col" style="left:113px"><h4>MY ACCOUNT</h4><a>Sign In</a><a>Register</a><a>Payment Confirmation</a><a>Reviews</a></div>
    <div class="f-pay" style="left:156px"><i style="width:7px"></i><i style="width:18px"></i><i style="width:15px"></i><i style="width:14px"></i><i style="width:10px"></i><i style="width:15px"></i></div>
    <div class="f-bottom">Copyright ©2021 Goobalo</div>
  </footer>
</section>

<!-- ===== WHOLESALE ===== -->
<section class="page" style="left:313px;top:836px;width:221px;height:320px">
  <header class="site-header">
    <span class="soc" style="left:12px"></span><span class="soc" style="left:22px"></span>
    <a class="nav-link" style="left:64px">HOME</a><a class="nav-link" style="left:83px">SHOP</a>
    <div class="brand" style="left:110px"><span class="mark"></span>Goobalo</div>
    <a class="nav-link" style="left:131px">ABOUT</a><a class="nav-link" style="left:151px">FAQ</a>
    <span class="login" style="left:180px"><i></i>Login</span>
    <svg class="cart" style="left:203px" viewBox="0 0 10 8"><path d="M0 2h10L8.5 8h-7z" fill="#06a55b"/></svg>
  </header>
  <p class="h-red rule" style="left:12px;top:33px">WHOLESALE</p>
  <span class="label" style="left:42px;top:46px">First Name</span><span class="label" style="left:115px;top:46px">Last Name</span>
  <div class="field" style="left:42px;top:50px;width:65px"></div><div class="field" style="left:115px;top:50px;width:65px"></div>
  <span class="label" style="left:42px;top:63px">How did you find out about us?</span><div class="field" style="left:42px;top:67px;width:138px;height:21px"></div>
  <span class="label" style="left:42px;top:93px">Brand/Store/Bar/Hotel Name</span><div class="field" style="left:42px;top:97px;width:138px"></div>
  <span class="label" style="left:42px;top:110px">Location (City/State)</span><div class="field" style="left:42px;top:114px;width:138px"></div>
  <span class="label" style="left:42px;top:127px">Phone Number</span><div class="field" style="left:42px;top:131px;width:138px"></div>
  <span class="label" style="left:42px;top:144px">Email</span><div class="field" style="left:42px;top:148px;width:138px"></div>
  <span class="label" style="left:42px;top:161px">Company Website</span><div class="field" style="left:42px;top:165px;width:138px"></div>
  <span class="label" style="left:42px;top:181px">What items of ours are you interested in carrying?</span>
  <span class="check" style="left:42px;top:191px"></span>
  <span class="check" style="left:42px;top:197px"></span>
  <span class="check" style="left:42px;top:203px"></span>
  <span class="check" style="left:42px;top:209px"></span>
  <span class="check" style="left:42px;top:215px"></span>
  <span class="check" style="left:42px;top:221px"></span>
  <span class="label" style="left:50px;top:221.3px">Organic Peanut Crackers Original (15 x 25g)</span>
  <div class="btn" style="left:42px;top:231px;width:65px">SUBMIT</div>
  <footer class="site-footer" style="top:251px;height:69px">
    <div class="f-brand"><i></i>Goobalo</div><div class="f-social"><i></i><i></i></div>
    <div class="f-col" style="left:50px"><h4>CUSTOMER CARE</h4><a class="u">Contact Us</a><a>How to Order</a><a>FAQ</a><a>Shipping</a><a>Terms &amp; Conditions</a><a>Wholesale</a></div>
    <div class="f-col" style="left:85px"><h4>ABOUT US</h4><a>Hello!</a><a>Store Locator</a></div>
    <div class="f-col" style="left:113px"><h4>MY ACCOUNT</h4><a>Sign In</a><a>Register</a><a>Payment Confirmation</a><a>Reviews</a></div>
    <div class="f-pay" style="left:156px"><i style="width:7px"></i><i style="width:18px"></i><i style="width:15px"></i><i style="width:14px"></i><i style="width:10px"></i><i style="width:15px"></i></div>
    <div class="f-bottom">Copyright ©2021 Goobalo</div>
  </footer>
</section>

</body>
</html>
```